Maple Hollow Comets

We are a travel softball organization based in Central IL. Girls are 8-14 yrs old. Looking for a modern website that is easily updated. Our current website is at www.maplehollowcomets.com. I want a tab for each team, 10U, 12U, 14U. I need a tab for pics. A tab for sponsors. A tap for files we have uploaded. And a about tab.

```html
<!DOCTYPE html>
<html lang="en">
<head>
<meta charset="utf-8">
<title>Maple Hollow Comets</title>
<link href="https://fonts.googleapis.com/css2?family=Raleway:wght@400;500;600;700&family=Roboto:wght@400;500&family=Open+Sans:ital,wght@0,400;1,400&display=swap" rel="stylesheet">
<style>
:root{
  --red:#e8212a;
  --dark:#2b2b2b;
  --nav:#333333;
  --text:#444444;
  --muted:#6a6a6a;
  --light:#f4f5f7;
  --line:#e2e2e2;
  --white:#ffffff;
}
*{margin:0;padding:0;box-sizing:border-box}
html,body{width:1200px;height:2550px;overflow:hidden;background:var(--white)}
body{position:relative;font-family:"Open Sans",sans-serif;color:var(--text)}
.abs{position:absolute}
/* header */
.topbar{left:0;top:0;width:1200px;height:62px;background:var(--white)}
.navbar{left:0;top:62px;width:1200px;height:51px;background:var(--nav)}
.brand{left:0;top:0;width:380px;height:113px}
.brand-name{left:120px;top:30px;width:200px;font-family:"Raleway",sans-serif;font-weight:700;font-size:24px;line-height:28px;color:var(--white);text-transform:uppercase}
.social-top{left:930px;top:14px;display:flex;gap:7px}
.social-top span{width:30px;height:30px;border:1.5px solid #c9c9c9;border-radius:50%}
.menu{left:392px;top:62px;width:730px;height:51px;display:flex;justify-content:space-between;align-items:center;list-style:none}
.menu li{font-family:"Raleway",sans-serif;font-weight:600;font-size:12px;color:var(--white);white-space:nowrap}
/* hero */
.hero{left:0;top:113px;width:1200px;height:504px;background:linear-gradient(160deg,#5d8a3a 0%,#7a9a50 30%,#b08962 55%,#9c7a5a 100%)}
.hero-card{left:85px;top:268px;width:352px;height:216px;background:rgba(60,60,60,.55);padding:24px 18px}
.hero-card h2{font-family:"Raleway",sans-serif;font-weight:500;font-size:24px;color:var(--white);text-transform:uppercase;margin-bottom:14px;white-space:nowrap}
.hero-card p{font-size:12px;line-height:20px;color:var(--white);margin-bottom:18px}
.hero-card a{font-size:12px;color:var(--white);text-decoration:underline;text-transform:uppercase}
/* section titles */
.sec-title{width:1200px;left:0;text-align:center;font-family:"Raleway",sans-serif;font-weight:500;font-size:25px;color:#4a4a4a;text-transform:uppercase}
.sec-sub{width:1200px;left:0;text-align:center;font-size:11.5px;color:var(--muted)}
/* about */
.about-title{left:87px;top:666px;font-family:"Raleway",sans-serif;font-weight:500;font-size:23px;color:#4a4a4a;text-transform:uppercase}
.about-lead{left:87px;top:710px;width:490px;font-family:"Raleway",sans-serif;font-weight:500;font-size:15px;line-height:27px;color:var(--red)}
.about-body{left:87px;top:776px;width:490px;font-size:11.5px;line-height:26px;color:var(--muted)}
.about-body p{margin-bottom:16px}
.btn-outline{left:87px;top:968px;width:129px;height:43px;border:1.5px solid var(--red);color:var(--red);font-family:"Raleway",sans-serif;font-weight:500;font-size:13px;display:flex;align-items:center;justify-content:center;text-transform:uppercase}
.about-photo{left:620px;top:668px;width:493px;height:319px;background:linear-gradient(180deg,#8fb4d6 0%,#6f9a5a 40%,#b89a78 75%,#9d8466 100%)}
/* schedule */
.schedule{left:0;top:1048px;width:1200px;height:532px;background:var(--light)}
.calendar{left:124px;top:1177px;width:509px;height:353px;background:var(--white);border:1px solid var(--line)}
.cal-head{height:63px;background:var(--red);color:var(--white);display:flex;align-items:center;justify-content:space-between;padding:0 30px;font-family:"Roboto",sans-serif}
.cal-head .yr{font-size:13px}
.cal-head .month{font-size:19px;font-weight:500}
.cal-grid{display:grid;grid-template-columns:repeat(7,1fr);font-family:"Roboto",sans-serif;font-size:14px;color:#333}
.cal-grid div{height:48px;display:flex;align-items:center;justify-content:center;border-right:1px solid var(--line);border-bottom:1px solid var(--line)}
.cal-grid div:nth-child(7n){border-right:none}
.cal-grid .dow{height:50px;font-weight:500;font-size:14.5px}
.cal-grid .today span{width:24px;height:24px;border-radius:50%;background:var(--red);color:var(--white);display:flex;align-items:center;justify-content:center;font-weight:500}
.event{left:705px;width:420px;height:84px}
.event-thumb{left:0;top:0;width:97px;height:84px;background:linear-gradient(160deg,#7b9b5e,#c7a88a 60%,#8a6a55)}
.event h4{position:absolute;left:119px;top:0;font-family:"Raleway",sans-serif;font-weight:600;font-size:12.5px;color:#444;text-transform:uppercase}
.event p{position:absolute;left:119px;font-style:italic;font-size:11.5px;color:var(--muted)}
/* gallery */
.video{left:87px;top:1704px;width:518px;height:318px;background:linear-gradient(170deg,#7a8e9c 0%,#8a9a80 40%,#5d7a45 70%,#6a6a5a 100%)}
.play{left:313px;top:1840px;width:64px;height:46px}
.thumb{width:241px;height:151px}
/* sponsors */
.sponsors{left:0;top:2060px;width:1200px;height:258px;background:var(--light)}
.sponsor{top:2175px;width:175px;height:98px;background:var(--white);border:1px solid #ececec;display:flex;align-items:center;justify-content:center}
/* footer */
.footer{left:0;top:2318px;width:1200px;height:232px;background:var(--dark);border-top:4px solid var(--red)}
.social-foot{left:390px;top:2348px;display:flex;gap:12px}
.social-foot span{width:60px;height:60px;border:1.5px solid #8a8a8a;border-radius:50%;display:flex;align-items:center;justify-content:center}
.foot-rule{left:87px;top:2422px;width:1026px;height:1px;background:#444}
.foot-menu{left:0;top:2446px;width:1200px;display:flex;justify-content:center;list-style:none;font-family:"Raleway",sans-serif;font-size:12px;color:#d8d8d8;text-transform:uppercase}
.foot-menu li+li::before{content:"|";margin:0 14px;color:#bbb}
.copyright{left:0;top:2488px;width:1200px;text-align:center;font-family:"Raleway",sans-serif;font-size:11.5px;color:#d8d8d8}
</style>
</head>
<body>
<header>
  <div class="abs topbar"></div>
  <div class="abs navbar"></div>
  <svg class="abs brand" viewBox="0 0 380 113" aria-hidden="true"><polygon points="0,0 318,0 378,113 0,113" fill="#e8212a"/></svg>
  <div class="abs brand-name">Maple Hollow Comets</div>
  <div class="abs social-top"><span></span><span></span><span></span><span></span><span></span></div>
  <ul class="abs menu">
    <li>HOME</li><li>10U</li><li>12U</li><li>14U</li><li>SPONSORS</li><li>ABOUT</li><li>SCHEDULE &amp; RESULTS</li><li>PICTURES/VIDEO</li><li>FILES</li><li>CONTACT US</li>
  </ul>
</header>

<section>
  <div class="abs hero" role="img" aria-label="Softball pitcher throwing to a batter on a sunny field"></div>
  <div class="abs hero-card">
    <h2>Maple Hollow Comets</h2>
    <p>Sed ut perspiciatis unde omnis iste natus error sit vol uptatem accusantium doloremque laudantium, totam rem aperiam, eaque ipsa quae</p>
    <a>Read More</a>
  </div>
</section>

<section>
  <h2 class="abs about-title">About Maple Hollow Comets</h2>
  <p class="abs about-lead">Maple Hollow Comets is a newly formed girls travel/competitive softball team based out of Maple Hollow, Illinois with girls</p>
  <div class="abs about-body">
    <p>Sed ut perspiciatis unde omnis iste natus error sit voluptatem accusantium doloremque laudantium, totam rem aperiam, eaque ipsa quae ab illo inventore veritatis et quasi archi-tecto beatae vitae dicta sunt explicabo. Nemo enim ipsam voluptatem quia voluptas sit magni dolores eos qui ratione voluptatem sequi nesciunt.</p>
    <p>Nemo enim ipsam voluptatem quia voluptas sit aspernatur aut odit aut fugit, sed quia con sequuntur magni dolores eos qui ratione voluptatem sequi nesciunt.</p>
  </div>
  <div class="abs btn-outline">Read More</div>
  <div class="abs about-photo" role="img" aria-label="Batter swinging at home plate with catcher crouched behind"></div>
</section>

<section>
  <div class="abs schedule"></div>
  <h2 class="abs sec-title" style="top:1078px">Schedule &amp; Results</h2>
  <p class="abs sec-sub" style="top:1120px">Sed ut perspiciatis unde omnis iste natus error sit voluptatem accusantium doloremque laudantium, totam rem aperiam,</p>
  <div class="abs calendar">
    <div class="cal-head"><span class="yr">2016</span><span class="month">MAY, 2017</span><span class="yr">2018</span></div>
    <div class="cal-grid">
      <div class="dow">SUN</div><div class="dow">MON</div><div class="dow">TUE</div><div class="dow">WED</div><div class="dow">THU</div><div class="dow">FRI</div><div class="dow">SAT</div>
      <div>1</div><div>2</div><div>3</div><div>4</div><div>5</div><div>6</div><div>7</div>
      <div>8</div><div class="today"><span>9</span></div><div>10</div><div>11</div><div>12</div><div>13</div><div>14</div>
      <div>15</div><div>16</div><div>17</div><div>18</div><div>19</div><div>20</div><div>21</div>
      <div>22</div><div>23</div><div>24</div><div>25</div><div>26</div><div>27</div><div>28</div>
      <div style="border-bottom:none">29</div><div style="border-bottom:none">30</div><div style="border-bottom:none">31</div><div style="border-bottom:none"></div><div style="border-bottom:none"></div><div style="border-bottom:none"></div><div style="border-bottom:none"></div>
    </div>
  </div>
  <div class="abs event" style="top:1190px">
    <div class="abs event-thumb" role="img" aria-label="Player portrait at the ballpark"></div>
    <h4>Comets Away vs Prairie Flyers</h4>
    <p style="top:28px">When : Wed,May 24,6.00Pm-9.00Pm</p>
    <p style="top:52px">Where : Ridgefield,IL 60000,USA</p>
  </div>
  <div class="abs event" style="top:1310px">
    <div class="abs event-thumb" role="img" aria-label="Team celebrating together"></div>
    <h4>Comets Away vs Prairie Flyers</h4>
    <p style="top:28px">When : Wed,May 24,6.00Pm-9.00Pm</p>
    <p style="top:52px">Where : Ridgefield,IL 60000,USA</p>
  </div>
  <div class="abs event" style="top:1430px">
    <div class="abs event-thumb" role="img" aria-label="Player fielding on the infield"></div>
    <h4>Comets Away vs Prairie Flyers</h4>
    <p style="top:28px">When : Wed,May 24,6.00Pm-9.00Pm</p>
    <p style="top:52px">Where : Ridgefield,IL 60000,USA</p>
  </div>
</section>

<section>
  <h2 class="abs sec-title" style="top:1616px">Video &amp; Photo Gallery</h2>
  <p class="abs sec-sub" style="top:1658px">Sed ut perspiciatis unde omnis iste natus error sit voluptatem accusantium doloremque laudantium, totam rem aperiam,</p>
  <div class="abs video" role="img" aria-label="Video still of the team posing in uniform outside a clubhouse"></div>
  <svg class="abs play" viewBox="0 0 64 46" aria-hidden="true"><circle cx="32" cy="23" r="23" fill="#e8212a"/><polygon points="26,13 26,33 42,23" fill="#ffffff"/></svg>
  <div class="abs thumb" style="left:619px;top:1704px;background:linear-gradient(170deg,#7fa060,#c9a888 60%,#a6856a)" role="img" aria-label="Player sliding into base"></div>
  <div class="abs thumb" style="left:872px;top:1704px;background:linear-gradient(170deg,#8ab070,#c8b8b0 50%,#6d8a52)" role="img" aria-label="Team group photo on the grass"></div>
  <div class="abs thumb" style="left:619px;top:1872px;background:linear-gradient(170deg,#9ab87a,#7fa060 40%,#c7ac8e)" role="img" aria-label="Batter running toward first base"></div>
  <div class="abs thumb" style="left:872px;top:1872px;background:linear-gradient(170deg,#5e6a5a,#7f8a78 50%,#3f4a3c)" role="img" aria-label="Player practicing in a batting cage"></div>
</section>

<section>
  <div class="abs sponsors"></div>
  <h2 class="abs sec-title" style="top:2086px">Our Sponsors</h2>
  <p class="abs sec-sub" style="top:2128px">Sed ut perspiciatis unde omnis iste natus error sit voluptatem accusantium doloremque laudantium, totam rem aperiam,</p>
  <div class="abs sponsor" style="left:104px"><svg width="80" height="74" aria-hidden="true"><rect x="10" y="2" width="60" height="70" rx="4" fill="#c62a2f"/></svg></div>
  <div class="abs sponsor" style="left:309px"><svg width="80" height="74" aria-hidden="true"><circle cx="40" cy="37" r="34" fill="#e7c64a"/></svg></div>
  <div class="abs sponsor" style="left:514px"><svg width="140" height="50" aria-hidden="true"><rect x="5" y="10" width="130" height="30" rx="4" fill="#b4205a"/></svg></div>
  <div class="abs sponsor" style="left:719px"><svg width="140" height="60" aria-hidden="true"><rect x="5" y="8" width="130" height="44" rx="22" fill="#3a4f8a"/></svg></div>
  <div class="abs sponsor" style="left:924px"><svg width="150" height="40" aria-hidden="true"><rect x="5" y="8" width="140" height="24" fill="#243c8c"/></svg></div>
</section>

<footer>
  <div class="abs footer"></div>
  <div class="abs social-foot">
    <span></span><span></span><span></span><span></span><span></span>
    <span><svg width="20" height="16" viewBox="0 0 20 16" aria-hidden="true"><rect x="1" y="1" width="18" height="14" rx="2" fill="none" stroke="#ffffff" stroke-width="1.6"/><polyline points="1.5,2 10,9 18.5,2" fill="none" stroke="#ffffff" stroke-width="1.6"/></svg></span>
  </div>
  <div class="abs foot-rule"></div>
  <ul class="abs foot-menu">
    <li>Home</li><li>10U</li><li>12U</li><li>14U</li><li>Sponsors</li><li>About</li><li>Schedule &amp; Results</li><li>Pictures/Video</li><li>Files</li><li>Contact Us</li>
  </ul>
  <p class="abs copyright">© Copyrights 2017 Maple Hollow Comets All Rights Reserved.</p>
</footer>
</body>
</html>
```